"Pay it Forward" stated in center, with circle design using 5 Icon photo and names.

Graphic Art Image :
Circle flow design of Pay It Forward example files enclosed.
Make graphic art design like ENCLOSED Center of Circle flow: "Pay it Forward Circle"
But with Circle flow of names/ icon's in hand written design ENCLOSED
Use the ENCLOSED Icon's for Business, School, Families, Communities, Dovrik Club
Try to use our green in ENCLSOED Logo Colors in your design---
Target Market(s)
Local Businesses, Schools
Industry/Entity Type
Fund Raising
Font styles to use
Sans Serif
Colors
00AB8E
00BBA5
67D7C9
C6EFE9
E9F9F6
Requirements
Must have
- Circle of Life type design

```html
<!DOCTYPE html>
<html lang="en">
<head>
<meta charset="utf-8">
<title>Pay It Forward</title>
<link rel="stylesheet" href="https://fonts.googleapis.com/css2?family=Archivo+Black&family=Poppins:wght@600;700&display=swap">
<style>
  :root {
    --backdrop: #2f2f2f;
    --page: #ffffff;
    --green-deep: #1f6b35;
    --green-mid: #4c9a50;
    --green-bright: #62b35a;
    --green-soft: #b9dc9c;
    --green-pale: #e3f1d6;
    --ring: #5aa561;
    --ink: #1b1b1b;
  }
  html, body {
    margin: 0;
    padding: 0;
    width: 1200px;
    height: 1200px;
    overflow: hidden;
    background: var(--backdrop);
  }
  .poster { display: block; width: 1200px; height: 1200px; }
  .node-ring { fill: var(--page); stroke: var(--ring); stroke-width: 4; }
  .node-label {
    font-family: "Poppins", sans-serif;
    font-weight: 600;
    font-size: 25px;
    fill: var(--ink);
    text-anchor: middle;
  }
  .flow-arrow { fill: none; stroke: var(--ring); stroke-width: 9; stroke-linecap: butt; }
  .flow-head { fill: none; stroke: var(--ring); stroke-width: 4; stroke-linejoin: miter; }
  .inner-orbit { fill: none; stroke: var(--ring); stroke-width: 2.5; stroke-dasharray: 6 6; }
  .headline-top {
    font-family: "Poppins", sans-serif;
    font-weight: 700;
    font-size: 72px;
    fill: var(--ink);
    text-anchor: middle;
  }
  .headline-main {
    font-family: "Archivo Black", sans-serif;
    font-size: 114px;
    fill: var(--ring);
    stroke: var(--ink);
    stroke-width: 3;
    paint-order: stroke;
    text-anchor: middle;
  }
  .brand-name {
    font-family: "Poppins", sans-serif;
    font-weight: 600;
    font-size: 31px;
    fill: var(--ink);
    text-anchor: middle;
  }
</style>
</head>
<body>
<svg class="poster" viewBox="0 0 1932 1932" xmlns="http://www.w3.org/2000/svg">
  <defs>
    <linearGradient id="waveTop" x1="0" y1="0" x2="1" y2="0">
      <stop offset="0" stop-color="var(--green-deep)"/>
      <stop offset="0.55" stop-color="var(--green-mid)"/>
      <stop offset="1" stop-color="var(--green-bright)"/>
    </linearGradient>
    <linearGradient id="waveBottom" x1="0" y1="0" x2="1" y2="0">
      <stop offset="0" stop-color="var(--green-bright)"/>
      <stop offset="0.5" stop-color="var(--green-mid)"/>
      <stop offset="1" stop-color="var(--green-deep)"/>
    </linearGradient>
    <clipPath id="pageClip"><rect x="384" y="148" width="1165" height="1634"/></clipPath>
  </defs>

  <g class="page" clip-path="url(#pageClip)">
    <rect x="384" y="148" width="1165" height="1634" fill="var(--page)"/>

    <g class="wave-top">
      <path d="M384 148 H1549 V372 C1350 300 1150 270 900 380 C700 470 520 500 384 502 Z" fill="var(--green-pale)"/>
      <path d="M384 148 H1549 V350 C1350 270 1150 250 900 350 C700 440 520 470 384 470 Z" fill="var(--green-soft)"/>
      <path d="M384 148 H1549 V320 C1350 230 1130 220 880 320 C690 400 520 430 384 437 Z" fill="url(#waveTop)"/>
    </g>

    <g class="wave-bottom">
      <path d="M384 1552 C600 1640 850 1700 1100 1660 C1300 1620 1430 1560 1549 1492 V1782 H384 Z" fill="var(--green-pale)"/>
      <path d="M384 1570 C600 1660 850 1720 1100 1685 C1300 1650 1430 1590 1549 1525 V1782 H384 Z" fill="var(--green-soft)"/>
      <path d="M384 1600 C600 1690 850 1745 1100 1712 C1300 1680 1430 1620 1549 1560 V1782 H384 Z" fill="url(#waveBottom)"/>
    </g>

    <circle class="inner-orbit" cx="960" cy="1000" r="293"/>

    <g class="flow">
      <path class="flow-arrow" d="M605 656 C680 590 760 545 842 522"/>
      <polyline class="flow-head" points="826,510 850,520 832,545"/>
      <path class="flow-arrow" d="M1165 540 C1250 580 1320 650 1368 722"/>
      <polyline class="flow-head" points="1368,700 1370,726 1346,716"/>
      <path class="flow-arrow" d="M1453 1072 C1425 1170 1380 1250 1322 1312"/>
      <polyline class="flow-head" points="1328,1288 1320,1315 1346,1312"/>
      <path class="flow-arrow" d="M1042 1474 C940 1490 860 1470 772 1434"/>
      <polyline class="flow-head" points="790,1424 768,1432 778,1454"/>
      <path class="flow-arrow" d="M530 1225 C490 1140 478 1040 484 955"/>
      <polyline class="flow-head" points="466,966 484,948 500,966"/>
    </g>

    <g class="node node-families">
      <circle class="node-ring" cx="995" cy="537" r="114"/>
      <circle cx="995" cy="537" r="98" fill="#e8efe6" role="img" aria-label="Illustration of a multi-generation family standing together"/>
      <text class="node-label" x="994" y="681">Families</text>
    </g>

    <g class="node node-schools">
      <circle class="node-ring" cx="1390" cy="887" r="114"/>
      <circle cx="1390" cy="887" r="98" fill="#f6ead6" role="img" aria-label="Icon of a school building with a sign"/>
      <text class="node-label" x="1397" y="1037">Schools</text>
    </g>

    <g class="node node-communities">
      <circle class="node-ring" cx="1177" cy="1393" r="114"/>
      <circle cx="1177" cy="1393" r="98" fill="#dfe9e6" role="img" aria-label="Illustration of a town square with houses, trees and people gathering"/>
      <text class="node-label" x="1179" y="1541">Communities</text>
    </g>

    <g class="node node-brand">
      <circle class="node-ring" cx="651" cy="1325" r="114"/>
      <text class="brand-name" x="651" y="1336">Dovrik Club</text>
    </g>

    <g class="node node-vendors">
      <circle class="node-ring" cx="554" cy="793" r="114"/>
      <circle cx="554" cy="793" r="98" fill="#f3e4d8" role="img" aria-label="Illustration of a shopkeeper standing outside an open storefront"/>
      <text class="node-label" x="557" y="945">Vendors</text>
    </g>

    <g class="headline">
      <text class="headline-top" x="970" y="966">Pay It</text>
      <text class="headline-main" x="961" y="1066">Forward</text>
    </g>
  </g>
</svg>
</body>
</html>
```